IT Services company general flyer

Looking for a printable US letter size flyer to give a brief overview of the services we offer. We also partner with another company for their services as well. Please check out our website at www.gizmobykellan.com and click on "Our Services" to learn about our services and visit www.bluefernguard,com and click on services to learn about their services. Several of our services do overlap, so they only need to be on the flyer once. Let me know if this is too much content and we need to weed some out. We do not want Home phone service on this flyer. The basic design of the flyer should mimic similar to the VOIP one you did for me for the colors and logo. Also check out the "Who Choose us" page on www.gizmobykellan.com to include some of that as well.

Target Market(s)

Targeting Small businesses that may not normally have a budget for their IT Services

Industry/Entity Type

It Service

Font styles to use
Serif
Sans Serif

Requirements
Must have
• Must include my logo, phone number and email/website address and must follow the same basic template of my previous flyers.

```html
<!DOCTYPE html>
<html lang="en">
<head>
<meta charset="utf-8">
<title>Gizmo by Kellan – IT Services Flyer</title>
<link href="https://fonts.googleapis.com/css2?family=Roboto:wght@400;500;700&display=swap" rel="stylesheet">
<style>
:root{
  --stage:#6b7f7c;
  --navy:#1a2a6c;
  --navy-deep:#0f1d52;
  --red:#8a1010;
  --white:#ffffff;
  --rule:rgba(255,255,255,.8);
}
*{margin:0;padding:0;box-sizing:border-box}
html,body{width:1200px;height:750px;overflow:hidden;background:var(--stage);font-family:"Roboto",Arial,sans-serif}
.flyer{position:absolute;left:365px;top:42px;width:471px;height:666px;overflow:hidden;background:var(--white)}
.header{position:absolute;left:0;top:0;width:100%;height:104px;background:var(--white)}
.brand-dot{position:absolute;left:37px;top:26px;width:62px;height:62px;border-radius:50%;background:var(--navy)}
.brand-rule{position:absolute;left:113px;top:18px;width:1px;height:80px;background:#c8c8c8}
.brand-name{position:absolute;left:122px;top:30px;font-weight:700;font-size:25px;line-height:26px;color:var(--navy)}
.hero-photo{position:absolute;left:0;top:104px;width:100%;height:562px;
  background:
    radial-gradient(ellipse 90px 22px at 414px 201px,rgba(200,225,255,.85) 0%,rgba(140,180,240,.35) 45%,rgba(0,0,0,0) 100%),
    linear-gradient(180deg,rgba(0,0,0,0) 188px,rgba(120,170,235,.35) 200px,rgba(120,170,235,.35) 206px,rgba(0,0,0,0) 220px),
    radial-gradient(ellipse 120px 150px at 270px 360px,rgba(170,140,130,.55) 0%,rgba(120,110,130,.25) 55%,rgba(0,0,0,0) 100%),
    radial-gradient(ellipse 140px 220px at 420px 120px,rgba(40,48,70,.75) 0%,rgba(0,0,0,0) 100%),
    linear-gradient(90deg,#1c3a78 0%,#24498a 35%,#2c5494 60%,#1e3366 100%)}
.feature-wing{position:absolute;left:300px;top:0;width:171px;height:104px;background:var(--navy);border-bottom-left-radius:70px}
.feature-wing-tail{position:absolute;left:390px;top:60px;width:81px;height:110px;background:var(--navy);border-bottom-left-radius:60px}
.feature-disc{position:absolute;left:268px;top:0;width:176px;height:176px;border-radius:50%;
  background:radial-gradient(circle at 58% 42%,#3a66c4 0%,#2a4aa0 35%,var(--navy) 70%,var(--navy-deep) 100%);
  border:3px solid var(--white)}
.services{position:absolute;left:33px;top:0;width:150px;color:var(--white)}
.service{position:absolute;left:0;width:143px;border-bottom:1px solid var(--rule);padding-bottom:5px}
.service h2{font-size:11px;font-weight:700;line-height:13px;margin-bottom:1px;white-space:nowrap}
.service p{font-size:9.2px;line-height:11.4px;white-space:nowrap}
.footer-tab{position:absolute;left:0;top:623px;width:119px;height:15px;background:var(--navy);
  clip-path:polygon(0 0,88% 0,100% 100%,0 100%);color:var(--white);font-size:6.8px;display:flex;align-items:center;padding-left:20px;gap:7px}
.footer-tab .social-box{width:8px;height:8px;background:var(--white);border-radius:1px}
.footer-band{position:absolute;left:0;top:637px;width:100%;height:29px;background:var(--red)}
.site{position:absolute;left:20px;top:638px;font-size:12.5px;letter-spacing:1.7px;color:var(--white);line-height:24px}
.contact-block{position:absolute;left:290px;top:620px;width:181px;height:46px;background:var(--navy);
  clip-path:polygon(12% 0,100% 0,100% 100%,0 100%)}
.contact-tab{position:absolute;left:214px;top:623px;width:88px;height:16px;background:var(--white);
  clip-path:polygon(5% 0,100% 0,95% 100%,0 100%);color:var(--navy-deep);font-size:10.5px;font-weight:500;text-align:center;line-height:16px}
.phone{position:absolute;left:322px;top:622px;display:flex;align-items:center;gap:5px;color:var(--white);font-size:17px;font-weight:700;line-height:20px}
.email{position:absolute;left:320px;top:642px;display:flex;align-items:center;gap:9px;color:var(--white);font-size:9.2px;line-height:14px}
</style>
</head>
<body>
<main class="flyer">
  <div class="hero-photo" role="img" aria-label="Businessman in a dark suit reaching out a hand toward a glowing digital interface with network icons, world map and binary code"></div>

  <header class="header">
    <div class="brand-dot"></div>
    <div class="brand-rule"></div>
    <div class="brand-name">GIZMO<br>BY KELLAN</div>
  </header>

  <div class="feature-wing"></div>
  <div class="feature-wing-tail"></div>
  <div class="feature-disc" role="img" aria-label="Desk telephone illustration on a blue circle"></div>

  <section class="services">
    <article class="service" style="top:139px">
      <h2>Managed IT Service</h2>
      <p>You need your IT systems for your<br>day to day work. Let us help<br>manage and protect them.</p>
    </article>
    <article class="service" style="top:226px">
      <h2>Business VOIP Phone Service</h2>
      <p>Reduce cost and improve commu-<br>nication for your business. Solutions<br>available for any size business from<br>1 phone to hundreds of phones.</p>
    </article>
    <article class="service" style="top:327px">
      <h2>Network Security</h2>
      <p>Worried about the latest ransom-<br>ware or crypto virus? We can help<br>design and protect your network.</p>
    </article>
    <article class="service" style="top:415px">
      <h2>Wireless Solutions</h2>
      <p>Is your wireless coverage spotty or<br>would you like to extend your<br>network or internet coverage to<br>another building?</p>
    </article>
    <article class="service" style="top:504px">
      <h2>Cloud Services</h2>
      <p>Want your own business email<br>service? Want to move to the cloud<br>for secure file storage and sharing?<br>Ask us about our complete cloud<br>solutions.</p>
    </article>
  </section>

  <div class="footer-tab">VISIT US AT <span class="social-box"></span></div>
  <div class="footer-band"></div>
  <div class="site">www.gizmobykellan.com</div>
  <div class="contact-block"></div>
  <div class="contact-tab">CONTACT US</div>
  <div class="phone">
    <svg width="14" height="14" viewBox="0 0 24 24" fill="none" stroke="#fff" stroke-width="2"><circle cx="12" cy="12" r="10.5"/><path d="M8 6.5l2 2.5-1.2 1.5a7 7 0 0 0 4.7 4.7l1.5-1.2 2.5 2-1.3 1.8c-4.8-.6-8.6-4.4-9.2-9.2z" fill="#fff" stroke="none"/></svg>
    555.014.0199
  </div>
  <div class="email">
    <svg width="10" height="8" viewBox="0 0 20 15"><rect width="20" height="15" rx="1.5" fill="#fff"/><path d="M1 1.5l9 7 9-7" fill="none" stroke="#1a2a6c" stroke-width="1.8"/></svg>
    sales@gizmobykellan.com
  </div>
</main>
</body>
</html>
```